Company notecard redesign

We'd like a redesign done of our company notecards. We use these cards to hand-write messages to clients/potential clients. This could be thank-you cards, congratulations cards, check-in cards, etc. Current cards are 5.5" x 8.5" and fold in half (you'll see the fold mark on the scanned image). We would like the new cards to not fold, and just be 5.5" x 4.25". We do like the little dog head you'll see on the inside notecard scan as the dog is our logo. I've also attached our "professional" logo with our new tagline. Address info you see on the outside notecard scan is correct.

Target Market(s)

Salesforce and CRM clients

Industry/Entity Type

It Company

Colors
3377b5
ffffff
fff8ef

Requirements
Must have
• Our logo, some contact info
Nice to have
• Dog head from our current notecard scan

```html
<!DOCTYPE html>
<html lang="en">
<head>
<meta charset="utf-8">
<title>Harlow Notecards</title>
<link href="https://fonts.googleapis.com/css2?family=Bebas+Neue&display=swap" rel="stylesheet">
<style>
  :root {
    --backdrop: #262626;
    --navy-top: #2e455c;
    --navy-bottom: #223345;
    --sky: #86abc6;
    --sky-deep: #6f9dbd;
    --paper: #f1f1ef;
    --ink: #1d2b3a;
  }
  * { margin: 0; padding: 0; box-sizing: border-box; }
  html, body {
    width: 1200px; height: 900px; overflow: hidden;
    background: var(--backdrop);
    font-family: "Bebas Neue", "Arial Narrow", sans-serif;
  }
  .card {
    position: absolute; left: 418px; width: 360px; height: 278px;
    box-shadow: 0 3px 8px rgba(0,0,0,.45);
    overflow: hidden;
  }
  .card-front { top: 154px; background: linear-gradient(180deg, var(--navy-top), var(--navy-bottom)); color: var(--sky); }
  .card-back { top: 463px; background: var(--paper); }

  .greeting {
    position: absolute; top: 124px; left: 0; width: 100%;
    text-align: center; font-size: 27px; letter-spacing: .5px;
  }
  .contact {
    position: absolute; right: 202px; top: 236px;
    text-align: right; font-size: 10px; line-height: 14px; letter-spacing: .4px;
  }
  .contact .gap { margin-left: 8px; }
  .brand {
    position: absolute; left: 243px; top: 228px;
  }
  .brand-name {
    display: flex; align-items: center; gap: 4px;
    font-size: 26px; line-height: 24px; letter-spacing: 1.5px; color: var(--sky);
  }
  .brand-dot { width: 12px; height: 12px; border-radius: 50%; background: var(--sky); }
  .brand-tagline { font-size: 6px; letter-spacing: .6px; margin-top: 1px; }

  .back-name {
    position: absolute; left: 23px; top: 237px;
    font-size: 28px; letter-spacing: 1.8px; color: var(--ink);
  }
  .corner-mark {
    position: absolute; right: -22px; bottom: -34px;
    width: 92px; height: 92px; border-radius: 50%;
    background: var(--sky-deep);
  }
</style>
</head>
<body>
  <section class="card card-front">
    <p class="greeting">Hello</p>
    <p class="contact">HARLOWCLOUD.COM<span class="gap">555.014.2280</span><br>1180 N BIRCH AVE LAKEVIEW IN 46000</p>
    <div class="brand">
      <div class="brand-name">HARLOW<span class="brand-dot"></span></div>
      <p class="brand-tagline">A CLOUD CONSULTING COMPANY</p>
    </div>
  </section>

  <section class="card card-back">
    <p class="back-name">HARLOW</p>
    <div class="corner-mark"></div>
  </section>
</body>
</html>
```